Capability Statement Document/Flyer

Take the existing words from the capability statement document (attached) and design a unique folder/flyer document for professional use. Maybe something like a trifold or bifold style. Use approved colours and logo as per the attached files.
Our company designs and builds small onshore gas processing plants.

```html
<!DOCTYPE html>
<html lang="en">
<head>
<meta charset="utf-8">
<title>Vantaro Capability Flyer</title>
<link href="https://fonts.googleapis.com/css2?family=Open+Sans:ital,wght@0,400;0,600;0,700;1,400&display=swap" rel="stylesheet">
<style>
:root{
  --stage:#555555;
  --teal:#0a7a68;
  --teal-text:#0d7b6a;
  --deep:#03363a;
  --mint:#acd8d0;
  --paper:#f6f6f6;
  --panel:#e8e8e8;
  --grey:#9a9a9a;
  --ink:#1f3b3b;
  --white:#ffffff;
}
*{margin:0;padding:0;box-sizing:border-box}
html,body{width:1200px;height:884px;overflow:hidden;background:var(--stage);font-family:'Open Sans',sans-serif}
.board{position:relative;width:1200px;height:884px}
.size-label{position:absolute;left:49px;top:26px;font-size:27px;color:#a9a9a9;font-weight:400}
.page{position:absolute;top:75px;width:536px;height:759px;background:var(--paper);overflow:hidden}
.page-front{left:50px}
.page-back{left:614px}
.abs{position:absolute}
.nowrap{white-space:nowrap}

/* front */
.brand{font-weight:700;color:var(--teal);letter-spacing:1px}
.hero-title{left:18px;top:84px;color:var(--white);font-size:14px;line-height:17px;font-weight:700}
.hero-title span{font-weight:400;display:block}
.h2{font-size:13.5px;font-weight:700;color:var(--deep);white-space:nowrap}
.intro{left:19px;top:184px;font-size:10.2px;line-height:13.7px;color:var(--teal-text);white-space:nowrap}
.intro b{color:var(--deep)}
.vision-top{left:19px;top:233px;width:294px;height:26px;background:var(--deep);color:var(--white);font-style:italic;font-size:10.5px;display:flex;align-items:center;justify-content:center}
.vision-bottom{left:19px;top:259px;width:294px;height:25px;background:var(--mint);color:var(--deep);font-weight:700;font-size:10.5px;display:flex;align-items:center;justify-content:center}
.photo{background:linear-gradient(160deg,#cfd9e0 0%,#b9c2c5 45%,#8d8a7c 75%,#b89f72 100%)}
.define{left:18px;top:317px;width:501px;height:60px;background:var(--mint);border-radius:3px;padding:3px 7px;font-size:10px;line-height:13.7px;color:var(--deep)}
.principles{left:18px;top:385px;width:501px;height:176px;border:1.5px solid var(--mint);border-radius:6px;background:rgba(255,255,255,.4)}
.num{width:13px;height:13px;background:var(--deep);color:var(--white);font-size:9px;font-weight:700;display:flex;align-items:center;justify-content:center}
.principle-text{font-size:10px;color:var(--deep);white-space:nowrap}
.objective{left:33px;top:506px;font-size:10px;line-height:13.6px;color:var(--deep);white-space:nowrap}
.roles-band{left:0;top:569px;width:536px;height:190px;background:var(--teal)}
.roles-tab{left:19px;top:569px;width:294px;height:25px;background:var(--deep);color:var(--white);font-weight:700;font-size:14px;padding-left:18px;display:flex;align-items:center}
.roles-strip{left:0;top:569px;width:19px;height:25px;background:var(--mint)}
.roles-table{left:17px;top:601px;width:502px;height:110px;background:var(--white);border-radius:4px;box-shadow:0 3px 0 #8c8c8c;overflow:hidden}
.roles-head{height:19px;background:var(--deep);color:var(--white);font-weight:700;font-size:10.5px;position:relative}
.roles-head span{position:absolute;top:2px;transform:translateX(-50%)}
.roles-col{position:absolute;top:24px;list-style:none;font-size:10px;color:var(--deep);line-height:15.5px;white-space:nowrap}
.roles-col li::before{content:"";display:inline-block;width:5px;height:5px;border-radius:50%;background:var(--grey);margin-right:9px;vertical-align:1px}
.site{font-weight:700;color:var(--white);white-space:nowrap}
.follow{font-size:9.5px;color:var(--white)}
.social{display:flex;gap:6px}
.social i{display:block;border-radius:50%;background:var(--white)}

/* back */
.panel-tab{height:22px;background:var(--deep);color:var(--white);font-weight:700;font-size:14px;display:flex;align-items:center;justify-content:center}
.list{list-style:none;font-size:8px;line-height:13px;color:var(--teal-text);white-space:nowrap}
.list li{position:relative;padding-left:16px}
.list li svg{position:absolute;left:0;top:2px}
.contact{left:273px;top:166px;width:252px;height:35px;background:var(--deep);color:var(--white);padding:4px 0 0 12px}
.contact .label{font-size:8.5px}
.contact .mail{font-size:11px;font-weight:700;display:flex;align-items:center;gap:5px;margin-top:1px}
.service{position:absolute;white-space:nowrap}
.service h3{font-size:10px;font-weight:700;color:var(--deep);line-height:12px}
.service p{font-size:7.8px;color:var(--teal-text);line-height:9.7px}
.svc-icon{position:absolute;width:22px;height:22px}
.rule{position:absolute;height:1px;background:#9fb0ad}
.people{left:11px;top:488px;width:514px;height:232px;background:var(--teal);border-radius:10px;overflow:hidden}
.people-tab{left:11px;top:488px;width:187px;height:20px;background:var(--deep);color:var(--white);font-weight:700;font-size:14px;padding-left:12px;display:flex;align-items:center;border-top-left-radius:10px}
.person-name{position:absolute;left:28px;width:80px;color:var(--white);font-size:9.5px;font-weight:700;line-height:10px}
.person-name span{display:block;font-weight:400;font-size:7.8px;line-height:11px;white-space:nowrap}
.person-bio{position:absolute;left:115px;width:392px;color:var(--white);font-size:7.8px;line-height:10.4px}
.person-bio b{display:block;font-weight:700;font-size:8px}
.person-rule{position:absolute;left:108px;width:1px;background:rgba(255,255,255,.5)}
.arrow-mark{position:absolute;left:11px;width:0;height:0;border-top:7px solid transparent;border-bottom:7px solid transparent;border-left:8px solid #cfe6e1}
.back-foot{left:0;top:725px;width:536px;height:34px;background:var(--deep)}
</style>
</head>
<body>
<div class="board">
  <div class="size-label">size A4</div>

  <section class="page page-front">
    <svg class="abs" style="left:0;top:0" width="536" height="160" viewBox="0 0 536 160">
      <defs>
        <linearGradient id="plantPhoto" x1="0" y1="0" x2="1" y2="1">
          <stop offset="0" stop-color="#c9d6e0"/>
          <stop offset=".45" stop-color="#a9b0b3"/>
          <stop offset=".75" stop-color="#8b8676"/>
          <stop offset="1" stop-color="#5d6a5f"/>
        </linearGradient>
      </defs>
      <polygon points="322,0 536,0 536,152 268,104" fill="url(#plantPhoto)" role="img" aria-label="Photo of an onshore gas processing plant with pipework"/>
      <polygon points="0,58 536,152 536,158 0,158" fill="var(--deep)"/>
      <polygon points="0,98 536,160 0,160" fill="var(--teal)"/>
      <polygon points="150,158 536,158 536,160 150,160" fill="var(--mint)"/>
    </svg>
    <div class="abs brand" style="left:90px;top:21px;width:173px;height:42px;display:flex;align-items:center;justify-content:center;font-size:31px">VANTARO</div>
    <div class="abs hero-title">SIMPLIFY<br>PROJECT<br>EXECUTION,<span>STREAMLINE OPERATIONS</span></div>

    <div class="abs h2" style="left:19px;top:163px">Who are Vantaro?</div>
    <p class="abs intro">Vantaro are a highly experienced team of Executive, Project, Construction, Commissioning and Operations<br>specialists who combine deep technical knowledge with proven leadership to deliver unique<br><b>Project Delivery Partner</b> services to organisations in Australia.</p>

    <div class="abs vision-top">Our vision is straightforward:</div>
    <div class="abs vision-bottom">Simplify Project Execution, Streamline Operations</div>
    <div class="abs photo" style="left:324px;top:230px;width:212px;height:80px" role="img" aria-label="Photo of a gas plant beside solar panels"></div>

    <div class="abs h2" style="left:19px;top:290px">What is a Project Delivery Partner?</div>
    <p class="abs define">A Project Delivery Partner (PDP) provides integrated project management along with technical,<br>commercial and delivery support services to help an organisation successfully deliver a project.<br>The PDP acts as the owner’s team while the owner retains accountability and key decision-making<br>authority.</p>

    <div class="abs principles"></div>
    <div class="abs h2" style="left:32px;top:396px">PDP Core Principles:</div>
    <div class="abs num" style="left:32px;top:420px">1</div><div class="abs principle-text" style="left:56px;top:419px">Owner controls the project</div>
    <div class="abs num" style="left:32px;top:441px">2</div><div class="abs principle-text" style="left:56px;top:440px">PDP enables delivery &amp; provides assurance</div>
    <div class="abs num" style="left:32px;top:463px">3</div><div class="abs principle-text" style="left:56px;top:462px">Contractors execute the work</div>
    <div class="abs h2" style="left:32px;top:485px">PDP Objective:</div>
    <p class="abs objective">Deliver the project safely, on schedule, within<br>budget and ready for operations; providing owner<br>capability throughout the project lifecycle.</p>

    <svg class="abs" style="left:0;top:0" width="536" height="570" viewBox="0 0 536 570">
      <path d="M406,464 L406,392 A72,72 0 0 0 343.6,500 Z" fill="var(--deep)"/>
      <path d="M406,464 L406,392 A72,72 0 0 1 468.4,500 Z" fill="var(--teal)"/>
      <path d="M406,464 L468.4,500 A72,72 0 0 1 343.6,500 Z" fill="var(--grey)"/>
      <line x1="406" y1="464" x2="406" y2="392" stroke="#fff" stroke-width="1.5"/>
      <line x1="406" y1="464" x2="468.4" y2="500" stroke="#fff" stroke-width="1.5"/>
      <line x1="406" y1="464" x2="343.6" y2="500" stroke="#fff" stroke-width="1.5"/>
      <circle cx="406" cy="464" r="8" fill="#fff"/>
      <g stroke="#fff" stroke-width=".8" fill="none">
        <path d="M382,498 H350 V534"/><path d="M430,498 H462 V534"/><path d="M406,505 V534"/>
      </g>
      <g fill="var(--deep)">
        <path d="M348,532 L352,532 L350,537 Z"/><path d="M404,532 L408,532 L406,537 Z"/><path d="M460,532 L464,532 L462,537 Z"/>
      </g>
      <line x1="328" y1="541" x2="482" y2="541" stroke="#9a9a9a" stroke-width=".8" stroke-dasharray="1.5 1.5"/>
      <rect x="328" y="558" width="154" height="3" fill="var(--mint)"/>
      <text x="369" y="433" fill="#fff" font-size="10.5" font-weight="700" text-anchor="middle" font-family="Open Sans, sans-serif">Owner</text>
      <text x="369" y="445" fill="#fff" font-size="8.5" text-anchor="middle" font-family="Open Sans, sans-serif">Operator</text>
      <text x="369" y="457" fill="#fff" font-size="8.5" text-anchor="middle" font-family="Open Sans, sans-serif">XYZ</text>
      <text x="438" y="425" fill="#fff" font-size="10.5" font-weight="700" text-anchor="middle" font-family="Open Sans, sans-serif">Project</text>
      <text x="438" y="436" fill="#fff" font-size="10.5" font-weight="700" text-anchor="middle" font-family="Open Sans, sans-serif">Delivery</text>
      <text x="438" y="447" fill="#fff" font-size="10.5" font-weight="700" text-anchor="middle" font-family="Open Sans, sans-serif">Partner</text>
      <text x="438" y="461" fill="#fff" font-size="8.5" text-anchor="middle" font-family="Open Sans, sans-serif">Vantaro</text>
      <text x="406" y="501" fill="#fff" font-size="10" font-weight="700" text-anchor="middle" font-family="Open Sans, sans-serif">Contractors</text>
      <text x="350" y="552" fill="var(--deep)" font-size="8" text-anchor="middle" font-family="Open Sans, sans-serif">Engineering</text>
      <text x="406" y="552" fill="var(--deep)" font-size="8" text-anchor="middle" font-family="Open Sans, sans-serif">Suppliers</text>
      <text x="462" y="552" fill="var(--deep)" font-size="8" text-anchor="middle" font-family="Open Sans, sans-serif">Execution</text>
    </svg>

    <div class="abs roles-band"></div>
    <div class="abs roles-strip"></div>
    <div class="abs roles-tab">PDP Roles &amp; Responsibilities:</div>
    <div class="abs roles-table">
      <div class="roles-head"><span style="left:105px">Owner</span><span style="left:356px">Vantaro Service</span></div>
      <ul class="roles-col" style="left:27px">
        <li>Sets Project Objectives</li><li>Approves Major Decisions</li><li>Holds Project Risk</li><li>Awards Contracts</li><li>Provides Funding</li>
      </ul>
      <div style="position:absolute;left:210px;top:25px;width:1px;height:78px;background:#8c8c8c"></div>
      <ul class="roles-col" style="left:249px;top:26px">
        <li>Develops Delivery Plans</li><li>Provides Recommendations</li><li>Identifies and Manages Risks</li><li>Manages Contractor Interfaces</li><li>Monitors Cost and Schedule Performance</li>
      </ul>
    </div>

    <svg class="abs" style="left:0;top:0" width="536" height="759" viewBox="0 0 536 759">
      <polygon points="389,759 536,727 536,759" fill="var(--mint)"/>
      <g fill="none" stroke="#fff" stroke-width="1.2">
        <circle cx="73" cy="735" r="12"/><ellipse cx="73" cy="735" rx="5" ry="12"/>
        <line x1="61" y1="735" x2="85" y2="735"/><path d="M63,728 H83 M63,742 H83"/>
      </g>
      <line x1="302" y1="719" x2="302" y2="752" stroke="#fff" stroke-width="1"/>
    </svg>
    <div class="abs site" style="left:100px;top:720px;font-size:21px">vantaro.com.au</div>
    <div class="abs follow" style="left:332px;top:713px">follow us</div>
    <div class="abs social" style="left:327px;top:729px"><i style="width:14px;height:14px"></i><i style="width:14px;height:14px"></i><i style="width:14px;height:14px"></i></div>
  </section>

  <section class="page page-back">
    <svg class="abs" style="left:0;top:0" width="536" height="72" viewBox="0 0 536 72">
      <rect width="536" height="70" fill="var(--teal)"/>
      <polygon points="0,25 250,70 170,70 0,45" fill="var(--deep)"/>
      <polygon points="0,52 100,70 0,70" fill="var(--mint)"/>
    </svg>
    <div class="abs" style="left:196px;top:18px;width:144px;height:35px;display:flex;align-items:center;justify-content:center;color:var(--white);font-weight:700;font-size:27px;letter-spacing:1px">VANTARO</div>

    <div class="abs" style="left:11px;top:70px;width:253px;height:131px;background:var(--panel)"></div>
    <div class="abs panel-tab" style="left:20px;top:78px;width:127px">PDP Benefits:</div>
    <ul class="abs list" style="left:20px;top:106px">
      <li><svg width="10" height="10" viewBox="0 0 10 10"><rect x=".5" y=".5" width="9" height="9" fill="none" stroke="var(--teal)"/><path d="M2,5 L4.3,7.3 L9.5,1" fill="none" stroke="var(--teal)" stroke-width="1.3"/></svg>Provides owners with access to experienced project delivery</li>
      <li>capability</li>
      <li><svg width="10" height="10" viewBox="0 0 10 10"><rect x=".5" y=".5" width="9" height="9" fill="none" stroke="var(--teal)"/><path d="M2,5 L4.3,7.3 L9.5,1" fill="none" stroke="var(--teal)" stroke-width="1.3"/></svg>Improved project controls and governance</li>
      <li><svg width="10" height="10" viewBox="0 0 10 10"><rect x=".5" y=".5" width="9" height="9" fill="none" stroke="var(--teal)"/><path d="M2,5 L4.3,7.3 L9.5,1" fill="none" stroke="var(--teal)" stroke-width="1.3"/></svg>Greater flexibility</li>
      <li>than traditional EPC delivery</li>
      <li><svg width="10" height="10" viewBox="0 0 10 10"><rect x=".5" y=".5" width="9" height="9" fill="none" stroke="var(--teal)"/><path d="M2,5 L4.3,7.3 L9.5,1" fill="none" stroke="var(--teal)" stroke-width="1.3"/></svg>Enhanced visibility and management of cost, schedule and risk</li>
      <li><svg width="10" height="10" viewBox="0 0 10 10"><rect x=".5" y=".5" width="9" height="9" fill="none" stroke="var(--teal)"/><path d="M2,5 L4.3,7.3 L9.5,1" fill="none" stroke="var(--teal)" stroke-width="1.3"/></svg>Scalable resources aligned with project phases</li>
    </ul>

    <div class="abs" style="left:273px;top:70px;width:252px;height:96px;background:var(--mint)"></div>
    <div class="abs panel-tab" style="left:281px;top:78px;width:127px">PDP Challenges:</div>
    <ul class="abs list" style="left:281px;top:106px">
      <li><svg width="9" height="9" viewBox="0 0 9 9"><circle cx="4.5" cy="4.5" r="3.8" fill="none" stroke="var(--teal)"/><path d="M2.5,2.5 L6.5,6.5 M6.5,2.5 L2.5,6.5" stroke="var(--teal)"/></svg>Owner retains significant delivery risk</li>
      <li><svg width="9" height="9" viewBox="0 0 9 9"><circle cx="4.5" cy="4.5" r="3.8" fill="none" stroke="var(--teal)"/><path d="M2.5,2.5 L6.5,6.5 M6.5,2.5 L2.5,6.5" stroke="var(--teal)"/></svg>Requires clear governance and decision-making processes</li>
      <li><svg width="9" height="9" viewBox="0 0 9 9"><circle cx="4.5" cy="4.5" r="3.8" fill="none" stroke="var(--teal)"/><path d="M2.5,2.5 L6.5,6.5 M6.5,2.5 L2.5,6.5" stroke="var(--teal)"/></svg>Multiple contractor interfaces require strong coordination</li>
      <li><svg width="9" height="9" viewBox="0 0 9 9"><circle cx="4.5" cy="4.5" r="3.8" fill="none" stroke="var(--teal)"/><path d="M2.5,2.5 L6.5,6.5 M6.5,2.5 L2.5,6.5" stroke="var(--teal)"/></svg>Success depends on collaborative Owner-PDP relationship</li>
    </ul>
    <div class="abs contact">
      <div class="label">FOR MORE INFORMATION CONTACT:</div>
      <div class="mail"><svg width="15" height="10" viewBox="0 0 15 10"><rect x=".5" y=".5" width="14" height="9" fill="none" stroke="#fff"/><path d="M.5,.5 L7.5,6 L14.5,.5" fill="none" stroke="#fff"/></svg>directors@vantaro.com.au</div>
    </div>

    <div class="abs h2" style="left:19px;top:203px;font-size:14px">PDP Services:</div>

    <div class="rule" style="left:28px;top:264px;width:238px"></div>
    <div class="rule" style="left:28px;top:307px;width:238px"></div>
    <div class="rule" style="left:28px;top:350px;width:238px"></div>
    <div class="rule" style="left:28px;top:394px;width:238px"></div>
    <div class="rule" style="left:28px;top:437px;width:238px"></div>
    <div class="rule" style="left:266px;top:264px;width:236px"></div>
    <div class="rule" style="left:266px;top:307px;width:236px"></div>
    <div class="rule" style="left:266px;top:350px;width:236px"></div>
    <div class="rule" style="left:266px;top:394px;width:236px"></div>
    <div class="rule" style="left:266px;top:437px;width:236px"></div>
    <div class="abs" style="left:266px;top:222px;width:1px;height:260px;background:#9fb0ad"></div>

    <svg class="svc-icon" style="left:47px;top:233px" viewBox="0 0 22 22" fill="none" stroke="var(--teal)" stroke-width="1.4"><rect x="3" y="3" width="16" height="18" rx="1"/><rect x="7" y="1" width="8" height="4"/><path d="M6,10 l1.5,1.5 l3,-3 M6,16 l1.5,1.5 l3,-3 M12,10 h5 M12,16 h5"/></svg>
    <svg class="svc-icon" style="left:47px;top:276px" viewBox="0 0 22 22" fill="var(--teal)"><path d="M9,1h4l.6,3 2.4,1 2.6,-1.7 2.8,2.8 -1.7,2.6 1,2.4 3,.6v4l-3,.6 -1,2.4 1.7,2.6 -2.8,2.8 -2.6,-1.7 -2.4,1 -.6,3h-4l-.6,-3 -2.4,-1 -2.6,1.7 -2.8,-2.8 1.7,-2.6 -1,-2.4 -3,-.6v-4l3,-.6 1,-2.4 -1.7,-2.6 2.8,-2.8 2.6,1.7 2.4,-1z M11,7a4,4 0 1,0 .01,0z" fill-rule="evenodd"/></svg>
    <svg class="svc-icon" style="left:45px;top:320px;width:26px" viewBox="0 0 26 22" fill="none" stroke="var(--teal)" stroke-width="1.3"><path d="M1,8 h5 l4,-2 h5 l4,2 h6 M1,8 v8 h4 l6,4 l3,-1 l5,-5 h6 v-6"/><path d="M10,11 l3,3 M13,10 l3,3"/></svg>
    <svg class="svc-icon" style="left:47px;top:362px" viewBox="0 0 22 22" fill="none" stroke="var(--teal)" stroke-width="1.4"><path d="M14,3 h-11 v18 h14 v-9"/><path d="M6,11 h8 M6,14 h8 M6,17 h6"/><circle cx="17" cy="5" r="4" fill="var(--teal)" stroke="none"/><path d="M15,5 l1.5,1.5 l2.5,-3" stroke="#fff"/></svg>
    <svg class="svc-icon" style="left:47px;top:406px" viewBox="0 0 22 22" fill="none" stroke="var(--teal)" stroke-width="1.5"><circle cx="11" cy="11" r="9.5"/><path d="M14,7.5 c-1,-1 -6,-1.5 -6,1.5 c0,3 6,1.5 6,4.5 c0,3 -5,2.5 -6.5,1.2 M11,4.5 v13"/></svg>
    <svg class="svc-icon" style="left:47px;top:448px" viewBox="0 0 22 22" fill="none" stroke="var(--teal)" stroke-width="1.4"><rect x="2" y="4" width="18" height="16" rx="1"/><path d="M2,8 h18 M6,2 v4 M16,2 v4"/><g fill="var(--teal)" stroke="none"><rect x="5" y="10" width="2" height="2"/><rect x="9" y="10" width="2" height="2"/><rect x="13" y="10" width="2" height="2"/><rect x="5" y="14" width="2" height="2"/><rect x="9" y="14" width="2" height="2"/><rect x="13" y="14" width="2" height="2"/></g></svg>
    <svg class="svc-icon" style="left:286px;top:233px" viewBox="0 0 22 22" fill="none" stroke="var(--teal)" stroke-width="1.5"><path d="M11,2 L21,20 H1 Z"/><path d="M11,8 v7"/><circle cx="11" cy="17.3" r=".8" fill="var(--teal)"/></svg>
    <svg class="svc-icon" style="left:286px;top:276px" viewBox="0 0 22 22" fill="none" stroke="var(--teal)" stroke-width="1.3"><path d="M1,7 L11,2 L21,7 Z M2,20 h18 M4,9 v9 M8,9 v9 M14,9 v9 M18,9 v9 M3,9 h16"/></svg>
    <svg class="svc-icon" style="left:286px;top:319px" viewBox="0 0 22 22" fill="none" stroke="var(--teal)" stroke-width="1.3"><path d="M5,21 v-19 M8,21 v-19 M5,5 h15 M3,5 h2 M5,8 l3,3 M8,8 l-3,3 M5,13 l3,3 M8,13 l-3,3 M17,5 v7"/><rect x="14" y="14" width="7" height="6"/></svg>
    <svg class="svc-icon" style="left:286px;top:362px" viewBox="0 0 22 22" fill="none" stroke="var(--teal)" stroke-width="1.3"><path d="M20,2 c-6,0 -11,5 -13,10 l3,3 c5,-2 10,-7 10,-13z"/><circle cx="14" cy="8" r="1.5"/><path d="M7,12 l-4,0 l3,-3 M10,15 l0,4 l3,-3 M5,16 l-3,4 M6,18 l-2,3"/></svg>
    <svg class="svc-icon" style="left:286px;top:404px" viewBox="0 0 22 22" fill="var(--teal)"><circle cx="11" cy="3" r="2"/><rect x="7" y="6" width="8" height="5"/><circle cx="4" cy="13" r="2"/><circle cx="11" cy="13" r="2"/><circle cx="18" cy="13" r="2"/><path d="M1,21 v-4 h6 v4z M8,21 v-4 h6 v4z M15,21 v-4 h6 v4z"/></svg>
    <svg class="svc-icon" style="left:286px;top:448px" viewBox="0 0 22 22" fill="var(--teal)"><path d="M20,3 l-3,3 -2,-1 -1,-2 3,-3 c-3,-1 -7,1 -6,5 l-10,10 c-1,1 -1,3 0,4 c1,1 3,1 4,0 l10,-10 c4,1 6,-3 5,-6z"/></svg>

    <div class="service" style="left:80px;top:228px"><h3>1. Project Management</h3><p>Planning, Reporting &amp; Delivery Leadership<br>from Concept to Completion</p></div>
    <div class="service" style="left:80px;top:271px"><h3>2. Engineering</h3><p>Concept Selection, Design Coordination,<br>Technical Assurance &amp; Value Engineering</p></div>
    <div class="service" style="left:80px;top:314px"><h3>3. Procurement</h3><p>Contracting Strategy, Tender Process<br>&amp; Supplier/Contractor Management</p></div>
    <div class="service" style="left:80px;top:357px"><h3>4. Approvals</h3><p>Land Access, Regulator Engagement, Safety<br>Case, Permits &amp; Licenses</p></div>
    <div class="service" style="left:80px;top:401px"><h3>5. Cost Control</h3><p>Budget Development, Forecasting &amp;<br>Management</p></div>
    <div class="service" style="left:80px;top:442px"><h3>6. Scheduling</h3><p>Master Schedule Development, WBS,<br>Resource Allocation, Monitoring &amp; Updating</p></div>
    <div class="service" style="left:323px;top:228px"><h3>7. Risk Management</h3><p>Risk Register, Identification, Mitigation &amp;<br>Reporting</p></div>
    <div class="service" style="left:323px;top:271px"><h3>8. Governance</h3><p>Framework, Stage Gates, Change control,<br>Reporting &amp; Decision Support</p></div>
    <div class="service" style="left:323px;top:314px"><h3>9. Construction</h3><p>Management &amp; Coordination of Contractor<br>Execution Teams</p></div>
    <div class="service" style="left:323px;top:357px"><h3>10. Commissioning &amp; Start-up</h3><p>Lead Commissioning &amp; Start-up, Completions System,<br>Bring the Facility to Steady-State</p></div>
    <div class="service" style="left:323px;top:401px"><h3>11. Operations Readiness</h3><p>People &amp; Organisation, Process &amp;<br>Procedures, Systems &amp; Technology</p></div>
    <div class="service" style="left:323px;top:442px"><h3>12. Operations &amp; Maintenance</h3><p>Monitor &amp; Operate Asset, Minimize<br>Downtime, Lowest Possible OPEX for Owner</p></div>

    <div class="abs people"></div>
    <div class="abs people-tab">Key Vantaro Personnel</div>
    <div class="person-rule" style="top:512px;height:200px"></div>
    <div class="arrow-mark" style="top:517px"></div>
    <div class="arrow-mark" style="top:553px"></div>
    <div class="arrow-mark" style="top:622px"></div>
    <div class="arrow-mark" style="top:679px"></div>

    <div class="person-name" style="top:513px">Daniel Hartley<br>Role<span>Executive Director</span></div>
    <div class="person-bio" style="top:512px"><b>35yrs Exp: Coralis Energy, Northsea Petro, KLMS, Apex Basin Energy</b>Extensive global energy industry experience, from frontline O&amp;M to the boardroom. Respected ‘C Suite’ leader with a track record of building high performing teams that deliver outstanding results.</div>

    <div class="person-name" style="top:549px">Graham Tolland<br>Role<span>Technical Director</span></div>
    <div class="person-bio" style="top:548px"><b>39yrs Exp: Coralis Energy, Northsea Petro, Gulf Petroleum Development, Meridian Oil, Harbour Gas Group, Eastgas, KLMS, Apex Basin Energy</b>Highly skilled &amp; experienced operations &amp; project management professional with 39 years’ experience in the global oil &amp; gas industry delivering multiple projects and establishing best in class operational assets. Deep knowledge of project management, construction, commissioning &amp; start-up including a global functional assurance role.</div>

    <div class="person-name" style="top:618px">Peter Ashworth<br>Role<span>Commercial Director</span></div>
    <div class="person-bio" style="top:617px"><b>40yrs Exp: Westreach, Orinex, Meridian Oil, KLMS, Apex Basin Energy</b>Senior Logistics &amp; Supply Chain Manager / Procurement Manager with strong operational, commercial, project management, negotiating &amp; relationship building skills. Experienced in operating complex and diverse logistics operations, significantly improving service levels<br>whilst reducing cost.</div>

    <div class="person-name" style="top:675px">Liam Corrigan<br>Role<span>Operations Director</span></div>
    <div class="person-bio" style="top:674px"><b>27yrs Exp: Meridian Oil, Harbour Gas Group, Eastgas, KLMS, Apex Basin Energy</b>27 years’ success leading operations, maintenance and commissioning teams on onshore and offshore oil and gas production platforms, FPSOs, gas processing, coal seam gas, refrigeration facilities, and chemical refineries. Results driven and enthusiastic Leader with a proven track record of delivery.</div>

    <div class="abs back-foot"></div>
    <svg class="abs" style="left:0;top:725px" width="536" height="34" viewBox="0 0 536 34">
      <polygon points="0,0 237,34 0,34" fill="var(--teal)"/>
      <g fill="none" stroke="#fff" stroke-width="1">
        <circle cx="286" cy="17" r="8"/><ellipse cx="286" cy="17" rx="3.5" ry="8"/><path d="M278,17 H294 M279.5,12.5 H292.5 M279.5,21.5 H292.5"/>
      </g>
      <line x1="432" y1="4" x2="432" y2="28" stroke="#fff" stroke-width="1"/>
    </svg>
    <div class="abs site" style="left:304px;top:733px;font-size:14px">vantaro.com.au</div>
    <div class="abs follow" style="left:452px;top:733px;font-size:6px">follow us</div>
    <div class="abs social" style="left:448px;top:743px;gap:4px"><i style="width:9px;height:9px"></i><i style="width:9px;height:9px"></i><i style="width:9px;height:9px"></i></div>
  </section>
</div>
</body>
</html>
```